Need website redesign!

I have a site, www.pinehavenfitcamp.example

I am looking to have it redesigned to make it simpler, and encourage people who hit the home page to click on a service, opt in, or contact me for more info. Having a video front and center with icons representing the services we offer around it may be a good idea, but I am open to YOUR design. Conversion is my goal. I want it to be friendly, but convey the fun and ENERGY of my bootcamp. Scrolling pics on home page so people can get a feel for our bootcamp is recommended as well.

```html
<!DOCTYPE html>
<html lang="en">
<head>
<meta charset="utf-8">
<title>Pine Haven Fit Camp</title>
<link href="https://fonts.googleapis.com/css2?family=Raleway:wght@400;500;600;700;800&display=swap" rel="stylesheet">
<style>
:root{
  --red:#ed1c24;
  --navy:#13142f;
  --black:#0b0b0b;
  --footer:#1d1d1d;
  --text:#222;
  --muted:#666;
  --card:#efedea;
  --line:#d8d8d8;
  --fb:#3b5998;
}
*{box-sizing:border-box;margin:0;padding:0}
html,body{width:696px;height:1200px;overflow:hidden;background:#fff}
body{font-family:'Raleway',sans-serif;color:var(--text);position:relative}
.abs{position:absolute}

/* header */
.site-header{position:absolute;left:0;top:0;width:696px;height:58px;background:var(--black)}
.brand{position:absolute;left:53px;top:0;width:65px;height:64px;background:var(--black);z-index:3;
  display:flex;flex-direction:column;align-items:center;justify-content:center;text-align:center;
  color:#fff;font-weight:800;font-size:9px;line-height:1.05;text-transform:uppercase;padding:4px}
.brand small{font-size:3.6px;font-weight:800;margin-top:3px;letter-spacing:.1px}
.main-nav{position:absolute;right:46px;top:25px;display:flex;gap:14px}
.main-nav a{color:var(--red);font-size:7.2px;font-weight:700;text-decoration:none;letter-spacing:.2px}
.main-nav a.active{color:#fff}

/* hero */
.hero{position:absolute;left:0;top:58px;width:696px;height:238px;border-top:2px solid var(--red);
  background:linear-gradient(100deg,#5a4a44 0%,#b23a38 30%,#8a6e66 55%,#c24a48 80%,#6b5550 100%)}
.hero-title{position:absolute;left:52px;top:136px;color:#fff;font-size:22px;font-weight:700;line-height:28px;
  text-shadow:0 1px 3px rgba(0,0,0,.45)}
.hero-form{position:absolute;left:458px;top:32px;width:149px;height:190px;background:rgba(225,225,225,.93)}
.hero-form .form-head{background:var(--navy);color:#fff;font-size:9.5px;font-weight:600;line-height:12px;padding:10px 14px;height:56px}
.hero-form label{display:block;font-size:6.5px;color:#111;margin:10px 0 3px 14px}
.hero-form .field{margin-left:14px;width:118px;height:18px;background:#fff;border:1px solid var(--red);font-size:6px;color:#aaa;padding:5px 6px}
.btn{display:inline-block;font-size:6.4px;font-weight:700;text-transform:uppercase;padding:4px 9px;color:#fff;letter-spacing:.1px}
.btn-dark{background:var(--navy)}
.btn-red{background:var(--red);font-weight:500;text-transform:none}
.hero-form .btn{margin:16px 0 0 14px;padding:6px 9px}

.offer-band{position:absolute;left:0;top:296px;width:696px;height:59px;background:var(--navy);color:#fff;
  font-size:16px;font-weight:500;text-align:center;line-height:59px}

/* intro */
.video{position:absolute;left:53px;top:380px;width:196px;height:152px;background:#111}
.video-title{position:absolute;left:7px;top:5px;color:#fff;font-size:7px}
.video-frame{position:absolute;left:55px;top:17px;width:88px;height:97px;background:linear-gradient(#d8bb86,#a8865a)}
.video-bar{position:absolute;left:0;top:132px;width:196px;height:2px;background:#555}
.video-bar:before{content:"";position:absolute;left:0;top:0;width:12px;height:2px;background:var(--red)}
.video-time{position:absolute;left:58px;top:139px;color:#ddd;font-size:5.5px}
.intro{position:absolute;left:278px;top:400px;width:270px}
.intro h1{font-size:16px;font-weight:500;color:#111;margin-bottom:10px}
.intro p{font-size:6.3px;line-height:12.7px;color:#333}
.intro .actions{margin-top:12px;display:flex;gap:6px}
.intro .btn{padding:4px 10px}
.btn-fb{background:var(--fb)}

/* services */
.section-head{position:absolute;left:53px;top:556px;width:596px;height:22px}
.section-head .rule{position:absolute;left:0;right:0;top:11px;height:1px;background:var(--line)}
.section-head h2{position:absolute;left:0;right:0;text-align:center;top:2px;font-size:15px;font-weight:500;color:#222}
.section-head h2 span{background:#fff;padding:0 18px}
.arrow{position:absolute;top:0;width:22px;height:22px;border-radius:50%;background:#eee}
.arrow svg{position:absolute;left:6px;top:6px}
.services{position:absolute;left:53px;top:605px;display:flex;gap:3.3px}
.service{width:82.4px;height:135px;background:var(--card);text-align:center}
.service .photo{height:75px}
.service h3{font-size:8.7px;font-weight:500;line-height:10.5px;height:30px;display:flex;align-items:center;justify-content:center;margin-top:3px;color:#222}
.service .btn{margin-top:5px;padding:3px 8px}

/* optin */
.optin{position:absolute;left:53px;top:761px;width:596px;height:101px;background:var(--card);border-bottom:1.5px solid var(--red)}
.optin h2{position:absolute;left:29px;top:18px;color:var(--red);font-size:14.5px;font-weight:700;line-height:19px}
.optin .group{position:absolute;top:30px}
.optin label{display:block;font-size:6.5px;color:#111;margin-bottom:3px}
.optin .field{width:118px;height:18px;background:#fff;border:1px solid var(--red);font-size:6px;color:#aaa;padding:5px 6px}
.optin .btn{position:absolute;left:488px;top:41px;padding:6px 9px}

.tagline{position:absolute;left:0;top:885px;width:696px;text-align:center;font-size:13px;line-height:16px;color:#333}
.tagline strong{color:var(--red);font-weight:700}

.gallery{position:absolute;left:52px;top:967px;display:flex;gap:5px}
.gallery .shot{width:83px;height:63px}
.gallery-cta{position:absolute;left:494px;top:967px;width:155px;height:63px;background:var(--red);color:#fff;
  font-size:13px;font-weight:700;line-height:16px;padding:9px 13px}
.gallery-cta svg{position:absolute;right:8px;top:13px}

/* footer */
.site-footer{position:absolute;left:0;top:1072px;width:696px;height:104px;background:var(--footer)}
.site-footer .brand{position:absolute;left:53px;top:-12px;height:65px}
.locations{position:absolute;left:54px;top:57px;color:#ddd;font-size:6.3px;line-height:9.5px}
.locations p{margin-bottom:2px}
.foot-nav{position:absolute;left:367px;top:20px;list-style:none}
.foot-nav li{font-size:6.3px;color:#ddd;line-height:12.5px}
.foot-nav:before{content:"";position:absolute;left:-19px;top:6px;width:10px;height:1.5px;background:var(--red)}
.map-label{position:absolute;left:466px;top:17px;color:#ddd;font-size:6.3px}
.map{position:absolute;left:466px;top:26px;width:183px;height:71px;background:linear-gradient(135deg,#e9e6df,#dcd8cf)}
.bottom-bar{position:absolute;left:0;top:1176px;width:696px;height:24px;background:var(--black);color:#ddd;font-size:6.3px}
.bottom-bar .copy{position:absolute;left:54px;top:8px}
.bottom-bar .legal{position:absolute;left:466px;top:8px}
.bottom-bar .legal span{margin:0 6px;color:#777}
.social{position:absolute;left:604px;top:5px;display:flex;gap:4px}
.social i{display:block;width:12px;height:12px;border-radius:50%;background:#555}
</style>
</head>
<body>

<header class="site-header">
  <div class="brand">Pine<br>Haven<br>Fit Camp<small>pinehavenfitcamp.example</small></div>
  <nav class="main-nav">
    <a class="active">HOME</a><a>SERVICES</a><a>CLASSES</a><a>ABOUT US</a><a>FAQ'S</a><a>CONTACT US</a>
  </nav>
</header>

<section class="hero" role="img" aria-label="Photo of a group class training with battle ropes in the gym">
  <h2 class="hero-title">Morning,<br>Evening and<br>Weekend Hours!</h2>
  <form class="hero-form">
    <div class="form-head">Leave your email for a FREE week of bootcamp, NO OBLIGATION</div>
    <label>Name</label><div class="field">Enter Your Name</div>
    <label>Email</label><div class="field">Enter Your Email ID</div>
    <span class="btn btn-dark">Get Started Now</span>
  </form>
</section>

<div class="offer-band">Fat Loss Bootcamps, Martial Arts, Yoga, Kids Fitness, Personal Training</div>

<div class="video">
  <div class="video-title">Dan R lost 15 pounds in just 17 sessi...</div>
  <div class="video-frame" role="img" aria-label="Video still of a client testimonial"></div>
  <div class="video-bar"></div>
  <svg class="abs" style="left:14px;top:138px" width="8" height="8" viewBox="0 0 8 8"><path d="M1 0L7 4L1 8Z" fill="#ccc"/></svg>
  <div class="video-time">0:00 / 0:16</div>
</div>

<section class="intro">
  <h1>What is Pine Haven Fit Camp</h1>
  <p>Lorem Ipsum is simply dummy text of the printing and typesetting industry. Lorem Ipsum has been the industry's standard dummy text ever since the 1500s, when .. unknown printer took a galley of type and scrambled it to make a type specimen book.Lorem Ipsum is simply standard dummy text ever since the 1500s, when .. unknown printer took a galley of type and scrambled it to make a type specimen book.</p>
  <div class="actions">
    <span class="btn btn-red">Read More</span>
    <span class="btn btn-dark">Get Started Now</span>
    <span class="btn btn-fb">Follow Us On Social</span>
  </div>
</section>

<div class="section-head">
  <div class="rule"></div>
  <h2><span>Our Services</span></h2>
  <div class="arrow" style="left:213px"><svg width="10" height="10" viewBox="0 0 10 10"><path d="M7 1L3 5L7 9" stroke="#bbb" stroke-width="1.3" fill="none"/></svg></div>
  <div class="arrow" style="left:361px"><svg width="10" height="10" viewBox="0 0 10 10"><path d="M3 1L7 5L3 9" stroke="#222" stroke-width="1.3" fill="none"/></svg></div>
</div>

<div class="services">
  <div class="service"><div class="photo" role="img" aria-label="Photo of bootcamp rope training" style="background:linear-gradient(#8a8a8a,#c0393a 60%,#333)"></div><h3>Boot Camp</h3><span class="btn btn-red">Read More</span></div>
  <div class="service"><div class="photo" role="img" aria-label="Photo of suspension strap training" style="background:linear-gradient(#9a9590,#4d4a48)"></div><h3>Personal<br>training</h3><span class="btn btn-red">Read More</span></div>
  <div class="service"><div class="photo" role="img" aria-label="Photo of a youth sports group" style="background:linear-gradient(#7a7088,#3c3848)"></div><h3>Youth Sports/<br>Agility</h3><span class="btn btn-red">Read More</span></div>
  <div class="service"><div class="photo" role="img" aria-label="Photo of a yoga instructor" style="background:linear-gradient(#3a2a24,#a5523e 70%,#c2263a)"></div><h3>Yoga</h3><span class="btn btn-red">Read More</span></div>
  <div class="service"><div class="photo" role="img" aria-label="Photo of a woman doing a plank" style="background:linear-gradient(#c9c4c0,#9c8a80)"></div><h3>Bride transform-<br>ation programs</h3><span class="btn btn-red">Read More</span></div>
  <div class="service"><div class="photo" role="img" aria-label="Photo of a martial arts belt and birthday cake" style="background:linear-gradient(#e0dcd6,#3a3a3a 55%,#d8b876)"></div><h3>Kids birthday<br>parties</h3><span class="btn btn-red">Read More</span></div>
  <div class="service"><div class="photo" role="img" aria-label="Photo of a corporate team group" style="background:linear-gradient(#c8ccd0,#6e7a86)"></div><h3>Corporate<br>Team Building</h3><span class="btn btn-red">Read More</span></div>
</div>

<section class="optin">
  <h2>Leave your email for a<br>FREE week of bootcamp,<br>NO OBLIGATION</h2>
  <div class="group" style="left:239px"><label>Name</label><div class="field">Enter Your Name</div></div>
  <div class="group" style="left:365px"><label>Email</label><div class="field">Enter Your Email ID</div></div>
  <span class="btn btn-dark">Get Started Now</span>
</section>

<p class="tagline">A fun, friendly, and effective place for you to shed serious fat,<br>build tight lean muscle, and have the time of your life doing it.<br>So...what are you waiting for? Register now and try us out <strong>RISK FREE!</strong></p>

<div class="gallery">
  <div class="shot" role="img" aria-label="Photo of a floor exercise" style="background:linear-gradient(#c6cbd0,#8bb04a)"></div>
  <div class="shot" role="img" aria-label="Photo of a group outdoors in the woods" style="background:linear-gradient(#8fa860,#3b5a7a)"></div>
  <div class="shot" role="img" aria-label="Photo of strap training" style="background:linear-gradient(#8c8784,#403c3a)"></div>
  <div class="shot" role="img" aria-label="Photo of outdoor training on grass" style="background:linear-gradient(#c8d2c0,#5f9a3c)"></div>
  <div class="shot" role="img" aria-label="Photo of a lunge exercise in the studio" style="background:linear-gradient(#d8dcd8,#7e8a8c)"></div>
</div>
<div class="gallery-cta">See Our<br>Complete<br>Photo Gallery
  <svg width="22" height="38" viewBox="0 0 22 38"><path d="M2 1L20 19L2 37" stroke="#fff" stroke-width="1.2" fill="none"/></svg>
</div>

<footer class="site-footer">
  <div class="brand">Pine<br>Haven<br>Fit Camp<small>pinehavenfitcamp.example</small></div>
  <div class="locations">
    <p>Ridgefield Martial Arts Studio<br>118 Orchard Lane, Maplecrest, ST 00101</p>
    <p>Pine Haven Fit Camp Main Studio<br>42 Brookside Drive, Suite B, Pine Haven, ST 00102</p>
  </div>
  <ul class="foot-nav"><li>Home</li><li>Services</li><li>Classes</li><li>About Us</li><li>Join Now</li><li>Contact Us</li></ul>
  <div class="map-label">Our Locations
    <svg width="7" height="5" viewBox="0 0 7 5" style="margin-left:3px"><path d="M0.5 0.5L3.5 4L6.5 0.5" stroke="#ddd" fill="none"/></svg>
  </div>
  <div class="map" role="img" aria-label="Map showing the studio location"></div>
</footer>

<div class="bottom-bar">
  <div class="copy">© 2014 Pine Haven Fit Camp</div>
  <div class="legal">Privacy Policy<span>|</span>Disclaimer</div>
  <div class="social"><i></i><i></i><i></i></div>
</div>

</body>
</html>
```